Corvelles Concept Stationery design

With my provided logo I need stationery design for business cards, envelope (#10), letterhead, fax sheet, memo sheet and 9'' x 12'' presentation folder. I would aIso need an email signature design included. PMS COLORS are : Pantone 541C et 299C. Looking for a bold look, minimalist yet eye-catching look.

```html
<!DOCTYPE html>
<html lang="en">
<head>
<meta charset="utf-8">
<title>Corvelles Concept Stationery</title>
<link href="https://fonts.googleapis.com/css2?family=Montserrat:wght@500&family=Arimo:wght@400;700&display=swap" rel="stylesheet">
<style>
  :root {
    --navy: #0b3d6e;
    --navy-deep: #083560;
    --navy-light: #164f80;
    --sky: #1fa0dc;
    --paper: #ffffff;
    --ink: #2b2b2b;
    --backdrop: #d3d3d8;
  }
  * { margin: 0; padding: 0; box-sizing: border-box; }
  html, body { width: 1200px; height: 1041px; overflow: hidden; }
  body {
    background: var(--backdrop);
    position: relative;
    font-family: "Arimo", Arial, sans-serif;
    color: var(--ink);
  }
  .piece { position: absolute; background: var(--paper); overflow: hidden; }
  .top-band { position: absolute; left: 0; top: 0; right: 0; height: 5px; background: var(--navy-deep); }

  .wordmark {
    position: absolute; display: flex; align-items: center;
    font-family: "Montserrat", sans-serif; font-weight: 500;
    color: var(--navy); white-space: nowrap; letter-spacing: 0.01em;
  }
  .wordmark .mark-square { border: 2px solid currentColor; flex: none; }
  .wordmark.on-dark { color: #ffffff; }

  /* Folder */
  .folder {
    left: 148px; top: 61px; width: 436px; height: 565px;
    background: linear-gradient(160deg, var(--navy-light) 0%, var(--navy) 55%, var(--navy-deep) 100%);
    border-radius: 3px;
  }
  .folder .wordmark { left: 210px; top: 87px; font-size: 15px; gap: 8px; }
  .folder .mark-square { width: 36px; height: 36px; border-width: 3px; }

  /* Letterhead */
  .letterhead { left: 617px; top: 81px; width: 420px; height: 545px; }
  .letterhead .wordmark { left: 42px; top: 33px; font-size: 12px; gap: 7px; }
  .letterhead .mark-square { width: 26px; height: 26px; }
  .contact-block { position: absolute; left: 304px; top: 32px; font-size: 5.4px; line-height: 7.6px; }
  .contact-block .lines { margin-top: 5px; }
  .contact-line { display: flex; align-items: center; gap: 3px; white-space: nowrap; }
  .contact-line svg { width: 5px; height: 5px; flex: none; }
  .recipient { position: absolute; left: 42px; top: 117px; font-size: 5.8px; line-height: 7.4px; }
  .letter-body { position: absolute; left: 42px; top: 179px; width: 336px; font-size: 5.3px; line-height: 7.3px; text-align: justify; }
  .letter-body p { margin-bottom: 7.3px; }
  .letter-body .salutation { font-weight: 700; margin-bottom: 7.5px; }
  .closing { position: absolute; left: 42px; top: 363px; font-size: 5.6px; }
  .signature-area { position: absolute; left: 42px; top: 378px; width: 72px; height: 30px; background: linear-gradient(90deg, #e6e8f2, #f4f5fa); }
  .signer { position: absolute; left: 42px; top: 414px; font-size: 5.8px; line-height: 7.4px; }
  .signer strong { font-weight: 700; }

  /* Envelope front */
  .envelope-front { left: 113px; top: 653px; width: 471px; height: 206px; }
  .envelope-front .wordmark { left: 22px; top: 28px; font-size: 12.5px; gap: 7px; }
  .envelope-front .mark-square { width: 28px; height: 28px; }
  .return-address { position: absolute; left: 22px; top: 178px; font-size: 5px; line-height: 7px; }

  /* Envelope back */
  .envelope-back { left: 617px; top: 653px; width: 471px; height: 206px; }
  .envelope-back svg.flap { position: absolute; left: 0; top: 0; }
  .flap-square { position: absolute; left: 225px; top: 20px; width: 20px; height: 20px; border: 2px solid #ffffff; }

  /* Business cards */
  .card-front { left: 410px; top: 888px; width: 175px; height: 101px; }
  .card-front .top-band { height: 3px; }
  .card-front .wordmark { left: 18px; top: 33px; font-size: 5.4px; gap: 3px; letter-spacing: 0; }
  .card-front .mark-square { width: 12px; height: 12px; border-width: 1.2px; }
  .card-address { position: absolute; right: 90px; top: 60px; font-size: 3.7px; line-height: 6px; text-align: right; white-space: nowrap; }
  .card-divider { position: absolute; left: 97px; top: 34px; width: 0.6px; height: 40px; background: #c9ccd3; }
  .card-person { position: absolute; left: 104px; top: 36px; font-size: 3.7px; line-height: 6px; }
  .card-person .person-name { font-weight: 700; color: var(--navy); font-size: 5.4px; line-height: 6px; }
  .card-person .role { color: #666; margin-bottom: 4px; }
  .card-person .contact-line svg { width: 3.5px; height: 3.5px; }
  .card-back { left: 617px; top: 888px; width: 175px; height: 101px; background: var(--navy); }
  .card-back .wordmark { left: 17px; top: 66px; font-size: 7px; gap: 4px; }
  .card-back .mark-square { width: 15px; height: 15px; border-width: 1.5px; }
</style>
</head>
<body>

<svg width="0" height="0" style="position:absolute">
  <defs>
    <symbol id="icon-phone" viewBox="0 0 10 10"><path d="M2 1l2 0 1 2.5-1.3 1a6 6 0 0 0 2.8 2.8l1-1.3 2.5 1v2c0 .5-.5 1-1 1A8 8 0 0 1 1 2c0-.5.5-1 1-1z" fill="#1fa0dc"/></symbol>
    <symbol id="icon-mail" viewBox="0 0 10 10"><rect x="0.5" y="2" width="9" height="6" fill="#1fa0dc"/><path d="M0.5 2l4.5 3.5 4.5-3.5" stroke="#fff" stroke-width="0.8" fill="none"/></symbol>
    <symbol id="icon-web" viewBox="0 0 10 10"><circle cx="5" cy="5" r="4.2" fill="none" stroke="#1fa0dc" stroke-width="1"/><ellipse cx="5" cy="5" rx="1.8" ry="4.2" fill="none" stroke="#1fa0dc" stroke-width="0.8"/><line x1="0.8" y1="5" x2="9.2" y2="5" stroke="#1fa0dc" stroke-width="0.8"/></symbol>
  </defs>
</svg>

<!-- Presentation folder -->
<section class="piece folder" aria-label="Presentation folder">
  <div class="wordmark on-dark"><span class="mark-square"></span>Corvelles Concept</div>
</section>

<!-- Letterhead -->
<section class="piece letterhead" aria-label="Letterhead">
  <div class="top-band"></div>
  <div class="wordmark"><span class="mark-square"></span>Corvelles Concept</div>
  <div class="contact-block">
    <div>2240 Rue des Ateliers<br>Laval, QC H7L 4B2</div>
    <div class="lines">
      <div class="contact-line"><svg><use href="#icon-phone"/></svg>450.555.0182</div>
      <div class="contact-line"><svg><use href="#icon-mail"/></svg>info@corvellesconcept.com</div>
      <div class="contact-line"><svg><use href="#icon-web"/></svg>www.corvellesconcept.com</div>
    </div>
  </div>
  <div class="recipient">
    Mr. Gerald Whitmore<br>President and CEO<br>Northvale Labs LLC.<br>880 Harbor Avenue, Suite 1200<br>New York, NY 10027
  </div>
  <div class="letter-body">
    <p class="salutation">Dear Mr. Whitmore:</p>
    <p>As Chairperson of the Corporate Conscience Campaign - Helping the Homeless in New York, I am writing this to thank you personally for your company's support in last month's fund-raising effort.</p>
    <p>As I indicated when we spoke on the phone two weeks ago, the campaign was considered a resounding success, raising a total of $1.65 million to-date, significantly exceeding our target of $1 million. Some donations are still trickling in, so we could end up close to a total of $2 million.</p>
    <p>Northvale Labs was an influential leader throughout the entire three-month campaign. In fact, we couldn't have succeeded without the generous support of your company, both financially, and through your organizational and administrative assistance. Your Team Leader, Helena Ortiz was particularly impressive, going above and beyond what we could have expected of someone performing as a volunteer while continuing on with her day-to-day duties. Please convey my special thanks to Helena.</p>
    <p>I would also ask you to convey my sincere thanks and congratulations to all of those other people in your company who contributed in any way to the Helping the Homeless Campaign. Please tell them that the sum of their contributions resulted in a major success that they should all be proud of taking part in.</p>
    <p>I believe that the 27 companies that participated in this effort have set a new standard for social responsibility in this community, and have set a powerful example that will inspire other companies and organizations to do the same.</p>
    <p>I look forward to seeing you at the Mayor's special thank you reception next month.</p>
  </div>
  <div class="closing">Yours sincerely,</div>
  <div class="signature-area" role="img" aria-label="Handwritten signature"></div>
  <div class="signer"><strong>Marcel Dufort</strong><br>Fundraising Chair</div>
</section>

<!-- #10 envelope, front -->
<section class="piece envelope-front" aria-label="Envelope front">
  <div class="top-band"></div>
  <div class="wordmark"><span class="mark-square"></span>Corvelles Concept</div>
  <div class="return-address">2240 Rue des Ateliers<br>Laval, QC H7L 4B2</div>
</section>

<!-- #10 envelope, back -->
<section class="piece envelope-back" aria-label="Envelope back">
  <svg class="flap" width="471" height="60" viewBox="0 0 471 60">
    <path d="M0 0 H471 L466 28 Q461 59 430 59 H41 Q10 59 5 28 Z" fill="var(--navy)"/>
  </svg>
  <span class="flap-square"></span>
</section>

<!-- Business card, front -->
<section class="piece card-front" aria-label="Business card front">
  <div class="top-band"></div>
  <div class="wordmark"><span class="mark-square"></span>Corvelles Concept</div>
  <div class="card-address">2240 Rue des Ateliers<br>Laval, QC H7L 4B2</div>
  <div class="card-divider"></div>
  <div class="card-person">
    <div class="person-name">ALEX MOREL</div>
    <div class="role">General Manager</div>
    <div class="contact-line"><svg><use href="#icon-phone"/></svg>450.555.0182</div>
    <div class="contact-line"><svg><use href="#icon-mail"/></svg>info@corvellesconcept.com</div>
    <div class="contact-line"><svg><use href="#icon-web"/></svg>www.corvellesconcept.com</div>
  </div>
</section>

<!-- Business card, back -->
<section class="piece card-back" aria-label="Business card back">
  <div class="wordmark on-dark"><span class="mark-square"></span>Corvelles Concept</div>
</section>

</body>
</html>
```